v-orn design for startup inpection service

building and pest inspections what i had in mind was v-orn in large print with prepurchase in small print directly under it and the small tm (tradmark) .Within the C I would like an eye but I don't want to take away from the C so maybe the eye would be done in a fine line?I would also like the Building and Pest inspections to be prominent and large .Have no idea of colors but do like black orange and silver

Target Market(s)

home buyers and realestate agents

Industry/Entity Type

Building

Contact Information for Business Card

v-orn prepurchase, Phone 0417382951, fax 02 93147708, email v-orn@mailbay.com.au ,building and pest inspections

Font styles to use
Sans Serif

Requirements
Must have
• bold color
• simple layout
• bold color
• uncluttered layout
Should not have
• contact details the same size as Building and Pest Inspections

```html
<!DOCTYPE html>
<html lang="en">
<head>
<meta charset="utf-8">
<title>v-orn prepurchase business card</title>
<link rel="stylesheet" href="https://fonts.googleapis.com/css2?family=Arimo:wght@400;700&display=swap">
<style>
  :root {
    --page-bg: #d9d3cb;
    --card-top: #f1eeeb;
    --card-mid: #e4e0dc;
    --name-ink: #17244f;
    --tagline-pink: #c63a82;
    --band-light: #2f4f86;
    --band-dark: #14234a;
    --band-line: #1d2f5c;
    --contact-ink: #c9adb2;
    --contact-fax: #c98f9b;
  }
  html, body {
    margin: 0;
    padding: 0;
    width: 1200px;
    height: 970px;
    overflow: hidden;
    background: var(--page-bg);
  }
  .business-card {
    position: absolute;
    left: 100px;
    top: 207px;
    width: 1000px;
    height: 555px;
    background: linear-gradient(180deg, var(--card-top) 0%, var(--card-mid) 60%);
    box-shadow: 0 10px 30px rgba(0,0,0,0.18);
    overflow: hidden;
  }
  .card-band {
    position: absolute;
    left: 0;
    top: 0;
    width: 1000px;
    height: 555px;
  }
  .business-name {
    position: absolute;
    left: 0;
    width: 1000px;
    margin: 0;
    text-align: center;
    font-family: "Arimo", sans-serif;
    font-weight: 700;
    color: var(--name-ink);
    line-height: 1;
  }
  .business-name-main {
    top: 40px;
    font-size: 124px;
  }
  .business-name-sub {
    top: 186px;
    font-size: 76px;
  }
  .tagline {
    position: absolute;
    left: 0;
    width: 1000px;
    top: 302px;
    margin: 0;
    text-align: center;
    font-family: "Arimo", sans-serif;
    font-size: 38px;
    line-height: 1;
    color: var(--tagline-pink);
  }
  .contact-list {
    position: absolute;
    left: 0;
    width: 1000px;
    top: 408px;
    margin: 0;
    padding: 0;
    list-style: none;
    text-align: center;
    font-family: "Arimo", sans-serif;
    font-size: 29px;
    line-height: 44px;
    color: var(--contact-ink);
  }
  .contact-list .contact-fax { color: var(--contact-fax); }
</style>
</head>
<body>
  <div class="business-card">
    <svg class="card-band" viewBox="0 0 1000 555" aria-hidden="true">
      <defs>
        <linearGradient id="bandFill" x1="0" y1="0" x2="0" y2="1">
          <stop offset="0" stop-color="var(--band-light)"/>
          <stop offset="1" stop-color="var(--band-dark)"/>
        </linearGradient>
      </defs>
      <path d="M0 333 H200 V362 L204 366 H810 L814 362 V333 H1000" fill="none" stroke="var(--band-line)" stroke-width="4"/>
      <path d="M0 344 H210 V374 H804 V344 H1000 V555 H0 Z" fill="url(#bandFill)"/>
    </svg>
    <p class="business-name business-name-main">v-orn</p>
    <p class="business-name business-name-sub">prepurchase</p>
    <p class="tagline">building and pest inspections</p>
    <ul class="contact-list">
      <li class="contact-phone">P : 0417382951</li>
      <li class="contact-fax">F : 02 93147708</li>
      <li class="contact-email">v-orn@mailbay.com.au</li>
    </ul>
  </div>
</body>
</html>
```